Self Defence Seminar Flyer

Need a flyer that will sell a seminar that will teach self defence techniques to customers. Needs to have a good image that will remind people about the dangerous world. The seminar is for men and women.

Needs to look professional.

I have attached the previous flyer we used. needs same information except without the same date and time for seminar.

Target Market(s)

Male and Females interested in learning how to defend themselves or family

Industry/Entity Type

Defence

Requirements
Must have
• A Image that reminds people of a dangerous situation

```html
<!DOCTYPE html>
<html lang="en">
<head>
<meta charset="utf-8">
<title>Self Defence Seminar</title>
<link href="https://fonts.googleapis.com/css2?family=Rubik+Dirt&family=Signika:wght@300;400;600&family=Bowlby+One&display=swap" rel="stylesheet">
<style>
  :root {
    --bg: #18191b;
    --red: #e4212b;
    --white: #ffffff;
    --leaf: #6f7d4a;
    --leaf-dark: #3d4a2c;
    --trunk: #8a7a66;
  }
  * { margin: 0; padding: 0; box-sizing: border-box; }
  html, body { width: 927px; height: 1200px; overflow: hidden; background: var(--bg); }
  .flyer { position: relative; width: 927px; height: 1200px; background: var(--bg); overflow: hidden; font-family: "Signika", sans-serif; color: var(--white); }

  .scene-photo {
    position: absolute; left: 0; top: 470px; width: 927px; height: 690px;
    background:
      radial-gradient(ellipse 220px 300px at 470px 360px, rgba(150,160,110,.55), transparent 70%),
      radial-gradient(ellipse 260px 220px at 760px 420px, rgba(120,140,80,.6), transparent 70%),
      radial-gradient(ellipse 220px 260px at 220px 330px, rgba(160,140,115,.55), transparent 70%),
      linear-gradient(180deg, var(--bg) 0%, #3a3f2f 18%, var(--trunk) 40%, var(--leaf) 62%, var(--leaf-dark) 78%, var(--bg) 100%);
  }
  .scene-photo::before, .scene-photo::after { content: ""; position: absolute; top: 0; bottom: 0; width: 240px; }
  .scene-photo::before { left: 0; background: linear-gradient(90deg, rgba(20,22,26,.9), transparent); }
  .scene-photo::after { right: 0; background: linear-gradient(270deg, rgba(20,22,26,.9), transparent); }

  .headline { position: absolute; left: 0; top: 0; width: 927px; height: 330px; }
  .headline text { font-family: "Rubik Dirt", sans-serif; fill: var(--red); }

  .points { position: absolute; top: 360px; list-style: none; }
  .points-left { left: 60px; width: 335px; }
  .points-right { left: 506px; width: 370px; }
  .points li { position: relative; padding-left: 22px; font-size: 18px; font-weight: 300; line-height: 29px; margin-bottom: 16px; }
  .points li::before {
    content: ""; position: absolute; left: 0; top: 9px; width: 11px; height: 11px; border-radius: 50%;
    background: radial-gradient(circle, var(--white) 0 2px, var(--red) 2.5px);
  }

  .booking { position: absolute; left: 0; top: 928px; width: 927px; text-align: center; }
  .cost { font-weight: 600; }
  .cost-label { color: var(--red); font-size: 21px; }
  .cost-value { font-size: 40px; }
  .cost-value sup { font-size: 20px; vertical-align: 16px; }
  .location { margin-top: 0; font-size: 17px; }
  .location-label { color: var(--red); font-weight: 600; }
  .banner-text { display: block; margin: 0 auto; }
  .banner-text text { font-family: "Bowlby One", sans-serif; fill: var(--white); }
  .banner-text .accent { fill: var(--red); }
  .cta { margin-top: 8px; }
  .website { margin-top: 4px; }

  .badges { position: absolute; left: 284px; top: 1108px; display: flex; gap: 4px; }
  .badge { height: 76px; border: 2px solid #cfcfcf; background: #0d0d0d; display: flex; align-items: center; justify-content: center; }
  .badge-team { width: 176px; font-weight: 600; font-size: 19px; color: var(--white); }
  .badge-mark { width: 70px; }
  .badge-mark span { width: 40px; height: 40px; border-radius: 50%; background: #c9a24a; }
  .badge-partner { width: 112px; }
  .badge-partner span { width: 60px; height: 54px; background: #2f5ea8; }

  .social { position: absolute; top: 1152px; font-size: 16px; font-weight: 300; }
  .social strong { font-weight: 600; font-size: 19px; margin-right: 6px; }
  .social-left { left: 52px; }
  .social-right { right: 64px; }
</style>
</head>
<body>
<main class="flyer">
  <div class="scene-photo" role="img" aria-label="Photo of a worried young woman in a green hoodie on a phone call, walking through a blurred park as a dark figure looms in the foreground"></div>

  <h1>
    <svg class="headline" viewBox="0 0 927 330" aria-label="Self Defence Seminar">
      <text x="120" y="150" font-size="140" textLength="690" lengthAdjust="spacingAndGlyphs">SELF DEFENCE</text>
      <text x="120" y="316" font-size="196" textLength="685" lengthAdjust="spacingAndGlyphs">SEMINAR</text>
    </svg>
  </h1>

  <ul class="points points-left">
    <li>Being a victim is a topic that people would like to avoid. Unfortunately. we live in an increasingly dangerous society for men and women alike. Learning to defend yourself is an important life skill.</li>
    <li>Spend 2 Hours with us learning some simple and effective Self Defence tactics that one-day may be needed to defend yourself or loved ones.</li>
  </ul>
  <ul class="points points-right">
    <li>Our aim is to teach you effective and efficient techniques and tactics to be able to defend yourself in a range of situations.</li>
    <li>Learn the same techniques and tactics that we have taught to individuals in Law enforcement. Security, and Military.</li>
    <li>We incorporate weapon defence, use of surroundings and psychological techniques in our classes.</li>
  </ul>

  <section class="booking">
    <p class="cost"><span class="cost-label">COST: </span><span class="cost-value">$60<sup>.00</sup></span></p>
    <p class="location"><span class="location-label">LOCATION: </span>Ironside Combat Gym (412 Harlow Rd. Westbrook NSW)</p>
    <svg class="banner-text cta" width="580" height="26" viewBox="0 0 580 26" aria-label="Sign up today by contacting us through our website">
      <text x="0" y="22" font-size="22" textLength="578" lengthAdjust="spacingAndGlyphs">SIGN UP TODAY BY CONTACTING US THROUGH OUR WEBSITE</text>
    </svg>
    <svg class="banner-text website" width="590" height="40" viewBox="0 0 590 40" aria-label="www.ironsidecombatacademy.com">
      <text x="0" y="34" font-size="34" textLength="588" lengthAdjust="spacingAndGlyphs">WWW.<tspan class="accent">IRONSIDECOMBATACADEMY</tspan>.COM</text>
    </svg>
  </section>

  <div class="badges">
    <div class="badge badge-team">Team Ironside</div>
    <div class="badge badge-mark"><span></span></div>
    <div class="badge badge-partner"><span></span></div>
  </div>

  <p class="social social-left"><strong>Socialbook</strong>/ironsideca</p>
  <p class="social social-right"><strong>Chirper</strong>#ironsideca</p>
</main>
</body>
</html>
```